Powerpoint and Word template required

We need PowerPoint and Word templates for all of our company branded materials and stationary. We have recently rebranded our website and would like something that is reflective of our new corporate branding. A sample of some of the documents we have created recently are attached and our website is below

http://corvanthealthcare.com.au/

The file 4089 Corvant_HPV_Rental_final.pdf was a document pulled together with a graphic designer recently which we think is a good starting point when thinking about the design we are after.

The word template will be used for all letters we send to clients and customers and we think we want the logo and ISO 9001 cert to only appear on the first page.

The powerpoint template has to be flexible as we use this for both marketing and training purposes. I have attached a couple of samples of the types of documents we create and note that these are very basic / crude and we would be looking for something that is a significant improvement on these

In the powerpoint template it would be good to have lots of standard layouts within the template, e.g. different 'standard layouts for multiple elements on a page including pictures and text etc.
Updates

Project Deadline Extended
Reason: Still looking for a professional yet modern template and important to us that we can see more tan just a title slide and the layout of the other slide master slides is very important to us. Many thanks, Dale

Industry/Entity Type

Healthcare

Font styles to use
Sans Serif

Colors
33a6d7

Requirements
Must have
• Templates must be versatile for use; powerpoint template must be able to be used for training materials and weel as marketing / pitch books.
• Word template must be able to be used as a basis for our corporate letter head through to RFP response type documents as well as Reference / Operating manual type of documents
• In terms of the design it must be consistent with our new corporate image which is best represented by our new website design; www.corvanthealthcare.com

```html
<!DOCTYPE html>
<html lang="en">
<head>
<meta charset="utf-8">
<title>Corvant Healthcare – Our Solutions</title>
<link href="https://fonts.googleapis.com/css2?family=Roboto+Condensed:wght@400;700&display=swap" rel="stylesheet">
<style>
  :root {
    --brand: #2b82cc;
    --brand-panel: #2e87d2;
    --brand-dark: #1f6fb4;
    --page: #eef2f6;
    --rule: #9fb3c6;
    --muted: #4a5560;
    --ink-dark: #1f2326;
    --white: #ffffff;
  }
  * { box-sizing: border-box; margin: 0; padding: 0; }
  html, body { width: 1200px; height: 900px; overflow: hidden; }
  body {
    font-family: "Roboto Condensed", "Arial Narrow", sans-serif;
    background: #d9dee3;
  }
  .slide {
    position: relative;
    width: 1200px;
    height: 900px;
    background: linear-gradient(180deg, #f4f7fa 0%, var(--page) 60%, #e6ebf0 100%);
    overflow: hidden;
  }
  .slide-title {
    position: absolute;
    left: 22px;
    top: 26px;
    font-size: 31px;
    font-weight: 700;
    color: var(--brand);
    letter-spacing: 0.3px;
  }
  .title-rule {
    position: absolute;
    left: 0;
    top: 65px;
    width: 256px;
    height: 2px;
    background: var(--rule);
  }
  .brand {
    position: absolute;
    right: 22px;
    top: 30px;
    display: flex;
    align-items: center;
    gap: 10px;
  }
  .brand-mark {
    width: 50px;
    height: 48px;
    background: var(--brand);
    border-radius: 4px;
  }
  .brand-name {
    font-size: 50px;
    font-weight: 700;
    color: var(--brand);
    line-height: 1;
  }
  .columns {
    position: absolute;
    left: 0;
    top: 120px;
    width: 1200px;
    display: grid;
    grid-template-columns: 396px 396px 396px;
    column-gap: 6px;
  }
  .column { display: flex; flex-direction: column; }
  .column-head {
    height: 100px;
    background: var(--brand);
    color: var(--white);
    font-size: 34px;
    font-weight: 700;
    display: flex;
    align-items: center;
    justify-content: center;
    text-align: center;
  }
  .column-photo { height: 358px; }
  .photo-feet { background: linear-gradient(180deg, #1c1c1c 0%, #4e4b48 45%, #8a8683 70%, #2a2a2a 100%); }
  .photo-hyperaemia { background: radial-gradient(ellipse at 55% 45%, #c8404e 0%, #d86a72 40%, #eab5ae 75%, #f2d3c9 100%); }
  .photo-erythema { background: linear-gradient(180deg, #dcdcd6 0%, #e7d2c9 35%, #e9c9c2 70%, #e3c2bb 100%); }
  .column-text {
    height: 224px;
    background: var(--brand-panel);
    color: var(--white);
    font-size: 24px;
    line-height: 1.4;
    text-align: center;
    padding: 26px 18px 0;
  }
  .footer-copyright {
    position: absolute;
    left: 0;
    top: 840px;
    width: 198px;
    height: 45px;
    background: var(--brand);
    color: var(--white);
    font-size: 20px;
    display: flex;
    align-items: center;
    justify-content: center;
  }
  .footer-url {
    position: absolute;
    left: 0;
    right: 0;
    top: 850px;
    text-align: center;
    font-size: 20px;
    color: var(--muted);
  }
  .page-number {
    position: absolute;
    left: 1147px;
    top: 847px;
    width: 45px;
    height: 42px;
    background: var(--ink-dark);
    color: var(--white);
    border-radius: 4px;
    font-size: 22px;
    font-weight: 700;
    display: flex;
    align-items: center;
    justify-content: center;
  }
</style>
</head>
<body>
<main class="slide">
  <h1 class="slide-title">OUR SOLUTIONS</h1>
  <div class="title-rule"></div>

  <div class="brand">
    <span class="brand-mark"></span>
    <span class="brand-name">Corvant</span>
  </div>

  <section class="columns">
    <article class="column">
      <h2 class="column-head">BLANCHING</h2>
      <div class="column-photo photo-feet" role="img" aria-label="Photograph of the backs of two heels showing whitened skin under compression"></div>
      <p class="column-text">Skin whitens under compression due to local occlusion or vasoconstriction of<br>the blood supply.</p>
    </article>
    <article class="column">
      <h2 class="column-head">BLANCHING</h2>
      <div class="column-photo photo-hyperaemia" role="img" aria-label="Close-up photograph of reddened skin showing reactive hyperaemia"></div>
      <p class="column-text">Courtesy of&nbsp; L. Hart<br>After prolonged and unrelieved pressure we get ‘Reactive Hyperaemia’</p>
    </article>
    <article class="column">
      <h2 class="column-head">BLANCHING ERYTHEMA?</h2>
      <div class="column-photo photo-erythema" role="img" aria-label="Photograph of reddened skin beside a measuring ruler"></div>
      <p class="column-text">Intact microcirculation is indicated when reddened skin – ‘Erythema’ - blanches or whitens, after light finger pressure is applied.</p>
    </article>
  </section>

  <div class="footer-copyright">Copyright text here</div>
  <div class="footer-url">||&nbsp;&nbsp; www.corvanthealthcare.com.au &nbsp;&nbsp;||</div>
  <div class="page-number">01</div>
</main>
</body>
</html>
```